Book cover design for my new Bankruptcy Law Book

Hi

I would like to get a unique and nice design for my new book titled: "Quiet Harbors and the Lantern Keeper's Final Season".

I like blue color. It will be in Arabic so I care the most about the design of the book cover and not the words on the cover as the printing company will handle the rest.

Much appreciated,

KAREEM HADDAWI

Colors
0692cd
33a6d7
86cae7
85abd2
3277b5
0255a3

Requirements
Must have
• Blue color
Nice to have
• pictures or shapes related to bankruptcy or insolvency

```html
<!DOCTYPE html>
<html lang="en">
<head>
<meta charset="utf-8">
<title>Quiet Harbors and the Lantern Keeper's Final Season — Cover</title>
<link rel="stylesheet" href="https://fonts.googleapis.com/css2?family=Bebas+Neue&display=swap">
<style>
  :root {
    --backdrop: #c4c4c4;
    --paper: #ffffff;
    --water-top: #1c7fc0;
    --water-light: #6fd6f5;
    --water-mid: #33b3e2;
    --water-deep: #2a8fc0;
    --floor-top: #4a8fb0;
    --floor-bottom: #245d85;
    --navy: #0a4a86;
    --title-white: #ffffff;
    --grid-line: rgba(190, 230, 245, 0.4);
    --trend-red: rgba(214, 86, 100, 0.7);
    --piggy-light: rgba(236, 170, 205, 0.95);
    --piggy-mid: rgba(214, 128, 175, 0.75);
    --figure-dark: rgba(28, 44, 64, 0.85);
  }
  * { margin: 0; padding: 0; box-sizing: border-box; }
  html, body {
    width: 1200px; height: 900px; overflow: hidden;
    background: var(--backdrop);
  }
  .canvas { position: relative; width: 1200px; height: 900px; }
  .book-cover {
    position: absolute; left: 355px; top: 40px;
    width: 490px; height: 820px; overflow: hidden;
    background: var(--paper);
    font-family: "Bebas Neue", "Arial Narrow", sans-serif;
  }
  .water {
    position: absolute; left: 0; top: 72px; width: 100%; height: 390px;
    background: linear-gradient(180deg, var(--water-top) 0%, #3fb8e6 8%, var(--water-light) 24%, var(--water-mid) 68%, var(--water-deep) 100%);
  }
  .bubbles { position: absolute; left: 0; top: 72px; width: 100%; height: 200px; }
  .piggy-bank {
    position: absolute; left: 112px; top: 24px; width: 176px; height: 190px;
    background:
      radial-gradient(ellipse 42% 44% at 50% 52%, var(--piggy-light) 0%, var(--piggy-mid) 55%, rgba(214,128,175,0.25) 80%, rgba(214,128,175,0) 100%);
  }
  .piggy-bank::after {
    content: ""; position: absolute; left: 0; right: 0; top: 52px; bottom: 0;
    background: linear-gradient(180deg, rgba(60,170,220,0.35), rgba(60,170,220,0.15));
    mask: radial-gradient(ellipse 42% 60% at 50% 40%, #000 60%, transparent 100%);
  }
  .waterline { position: absolute; left: 0; top: 64px; width: 100%; height: 18px; }
  .chart-floor {
    position: absolute; left: 0; top: 448px; width: 100%; height: 372px;
    background: linear-gradient(180deg, var(--floor-top) 0%, var(--floor-bottom) 100%);
  }
  .chart-floor svg { position: absolute; inset: 0; }
  .title {
    position: absolute; left: 20px; right: 20px; top: 236px;
    text-align: center; white-space: nowrap; font-weight: 400;
  }
  .title-line-1 { display: block; color: var(--title-white); font-size: 60px; line-height: 0.92; }
  .title-line-2 { display: block; color: var(--navy); font-size: 57px; line-height: 0.92; }
  .title-line-3 { display: block; color: var(--navy); font-size: 150px; line-height: 0.84; }
  .figure {
    position: absolute; left: 10px; top: 500px; width: 110px; height: 270px;
    background: radial-gradient(ellipse 40% 50% at 50% 50%, var(--figure-dark) 0%, rgba(28,44,64,0.55) 55%, rgba(28,44,64,0) 100%);
  }
  .author {
    position: absolute; left: 0; right: 0; top: 752px;
    text-align: center; color: var(--title-white);
    font-size: 34px; letter-spacing: 0.5px;
  }
</style>
</head>
<body>
<main class="canvas">
  <section class="book-cover">
    <div class="water"></div>
    <svg class="bubbles" viewBox="0 0 490 200" aria-hidden="true">
      <g fill="rgba(255,255,255,0.45)">
        <circle cx="40" cy="30" r="2"/><circle cx="320" cy="60" r="2.5"/>
        <circle cx="380" cy="25" r="1.5"/><circle cx="455" cy="120" r="2"/>
        <circle cx="90" cy="140" r="1.5"/><circle cx="270" cy="150" r="2"/>
      </g>
    </svg>
    <div class="piggy-bank" role="img" aria-label="Pink piggy bank sinking below the water surface"></div>
    <svg class="waterline" viewBox="0 0 490 18" preserveAspectRatio="none" aria-hidden="true">
      <path d="M0 9 Q30 4 60 9 T120 9 T180 8 T240 9 T300 8 T360 9 T420 8 T490 9 V18 H0 Z" fill="rgba(21,112,179,0.85)"/>
    </svg>

    <div class="chart-floor">
      <svg viewBox="0 0 490 372" preserveAspectRatio="none" aria-hidden="true">
        <defs>
          <pattern id="grid" width="30" height="30" patternUnits="userSpaceOnUse">
            <path d="M30 0 V30 M0 30 H30" stroke="var(--grid-line)" stroke-width="1" fill="none"/>
          </pattern>
        </defs>
        <rect width="490" height="372" fill="url(#grid)"/>
        <polygon points="150,372 240,150 300,230 380,170 470,300 490,372" fill="rgba(30,60,90,0.25)"/>
        <polygon points="0,372 0,325 60,325 90,372" fill="rgba(20,45,70,0.3)"/>
        <polyline points="10,13 125,41 217,251 361,162 412,302 476,288"
                  fill="none" stroke="var(--trend-red)" stroke-width="5" stroke-linejoin="round"/>
        <g fill="none" stroke="rgba(220,240,250,0.8)" stroke-width="2">
          <circle cx="10" cy="13" r="6"/>
          <circle cx="125" cy="41" r="6"/>
          <circle cx="361" cy="162" r="6"/>
          <circle cx="476" cy="288" r="6"/>
        </g>
      </svg>
    </div>

    <h1 class="title">
      <span class="title-line-1">Quiet Harbors and the</span>
      <span class="title-line-2">Lantern Keeper's Final</span>
      <span class="title-line-3">Season</span>
    </h1>

    <div class="figure" role="img" aria-label="Businessman in a suit leaning on the chart with head bowed"></div>

    <p class="author">KAREEM HADDAWI</p>
  </section>
</main>
</body>
</html>
```